Modern Lawfirm Business Card Design

We're looking for a business card to incorporate the newly created logo we had made.

Ideally looking for a law firm business card demonstrating, modern, minimalist, strong/bold design.

I'm open to any design honestly, but nothing "flashy".

Target Market(s)

Immigration law, family immigration, humanitarian, general legal

Industry/Entity Type

Law Firm

Contact Information for Business Card

Please use dummy information, name, street address, city, state, phone number, email, website.

Font styles to use
Serif
Sans Serif

Requirements
Must have
• Please use dummy information, name, street address, city, state, phone number, email, website.

```html
<!DOCTYPE html>
<html lang="en">
<head>
<meta charset="utf-8">
<title>Calloway Immigration Law – Business Card</title>
<link rel="stylesheet" href="https://fonts.googleapis.com/css2?family=Roboto:wght@400;500;700&display=swap">
<style>
  :root {
    --brand-blue: #17467f;
    --paper: #ffffff;
    --backdrop: #d4d4d4;
    --ink: #17467f;
  }
  * { box-sizing: border-box; margin: 0; padding: 0; }
  html, body {
    width: 1200px; height: 800px; overflow: hidden;
    background: var(--backdrop);
    font-family: "Roboto", Arial, sans-serif;
  }
  .stage {
    width: 1200px; height: 800px;
    display: flex; align-items: center; justify-content: center; gap: 40px;
  }
  .card {
    width: 540px; height: 309px; position: relative; overflow: hidden;
    box-shadow: 0 6px 18px rgba(0,0,0,0.18);
  }

  /* Front */
  .card--front { background: var(--paper); }
  .front__edge {
    position: absolute; left: 0; top: 0; bottom: 0; width: 34px;
    background: var(--brand-blue);
  }
  .front__content { position: absolute; left: 66px; top: 36px; right: 30px; }
  .wordmark {
    display: flex; align-items: center; gap: 10px;
    color: var(--ink); font-weight: 700; font-size: 26px; letter-spacing: 1px;
    text-transform: uppercase;
  }
  .wordmark__mark { width: 14px; height: 14px; background: currentColor; flex: none; }
  .person { margin-top: 26px; display: flex; align-items: flex-start; gap: 10px; color: var(--ink); }
  .person__name { font-weight: 700; font-size: 21px; line-height: 1; }
  .person__title { font-weight: 500; font-size: 15px; margin-top: 4px; }
  .contacts { list-style: none; margin-top: 26px; color: var(--ink); }
  .contacts li {
    display: flex; align-items: center; gap: 10px;
    font-size: 14px; font-weight: 500; line-height: 1; margin-bottom: 10px;
  }
  .icon {
    width: 20px; height: 20px; border-radius: 50%; flex: none;
    background: var(--brand-blue); display: flex; align-items: center; justify-content: center;
  }
  .icon svg { width: 12px; height: 12px; }

  /* Back */
  .card--back {
    background: var(--brand-blue); color: var(--paper);
    display: flex; flex-direction: column; align-items: center; justify-content: center;
  }
  .card--back .wordmark { color: var(--paper); font-size: 30px; }
  .card--back .wordmark__mark { width: 16px; height: 16px; }
  .back__web {
    position: absolute; bottom: 32px; right: 38px;
    font-size: 14px; font-weight: 500;
  }
</style>
</head>
<body>
<main class="stage">

  <section class="card card--front" aria-label="Business card front">
    <div class="front__edge"></div>
    <div class="front__content">
      <div class="wordmark"><span class="wordmark__mark"></span>Calloway Immigration Law</div>

      <div class="person">
        <span class="icon" aria-hidden="true">
          <svg viewBox="0 0 12 12"><circle cx="6" cy="4" r="2.3" fill="#fff"/><path d="M1.8 11c.4-2.4 2.1-3.6 4.2-3.6s3.8 1.2 4.2 3.6z" fill="#fff"/></svg>
        </span>
        <div>
          <div class="person__name">YOUR NAME</div>
          <div class="person__title">Your Title</div>
        </div>
      </div>

      <ul class="contacts">
        <li>
          <span class="icon" aria-hidden="true"><svg viewBox="0 0 12 12"><path d="M6 1a3.4 3.4 0 0 0-3.4 3.4C2.6 7 6 11 6 11s3.4-4 3.4-6.6A3.4 3.4 0 0 0 6 1z" fill="#fff"/><circle cx="6" cy="4.4" r="1.2" fill="#17467f"/></svg></span>
          2280 Harlow Avenue Suite 410 Dallas, TX 75219
        </li>
        <li>
          <span class="icon" aria-hidden="true"><svg viewBox="0 0 12 12"><path d="M3 1.2l1.7 2.3-1 1.2c.7 1.4 1.7 2.4 3.1 3.1l1.2-1L10.3 8.5 9.5 10.6C5.2 10.3 1.7 6.8 1.4 2.5z" fill="#fff"/></svg></span>
          (214) 555-0147
        </li>
        <li>
          <span class="icon" aria-hidden="true"><svg viewBox="0 0 12 12"><rect x="1.5" y="3" width="9" height="6.5" rx="0.8" fill="#fff"/><path d="M1.8 3.4 6 6.7l4.2-3.3" stroke="#17467f" stroke-width="0.9" fill="none"/></svg></span>
          hello@callowayimmigration.com
        </li>
        <li>
          <span class="icon" aria-hidden="true"><svg viewBox="0 0 12 12"><circle cx="6" cy="6" r="4.4" stroke="#fff" stroke-width="1" fill="none"/><ellipse cx="6" cy="6" rx="1.9" ry="4.4" stroke="#fff" stroke-width="0.9" fill="none"/><path d="M1.6 6h8.8" stroke="#fff" stroke-width="0.9"/></svg></span>
          www.callowayimmigration.com
        </li>
      </ul>
    </div>
  </section>

  <section class="card card--back" aria-label="Business card back">
    <div class="wordmark"><span class="wordmark__mark"></span>Calloway Immigration Law</div>
    <div class="back__web">www.callowayimmigration.com</div>
  </section>

</main>
</body>
</html>
```